Business cards/ stationery design for a transport consultancy
Freight Lantern
Business cards/ stationery design for a transport consultancy - Consulting
Creative Brief
Use standard fonts
Use either logo font (EUROSTILE LT STD) or complimentary font type
Simple
Declan Brolly
Managing Director
Ground Floor 27/ 28 Wexholm Yard Dublin 2 Ireland
dbrolly@freightlantern.com
www.freightlantern.com
Registered office address, and company registration number will need to be included as a footer at bottom of letter template.
Emphasis on designs should be on conveying a professional image.

```html
<!DOCTYPE html>
<html lang="en">
<head>
<meta charset="utf-8">
<title>Freight Lantern – Business Card</title>
<link rel="stylesheet" href="https://fonts.googleapis.com/css2?family=Arimo:wght@400;700&display=swap">
<style>
  :root {
    --bg: #2a2c30;
    --blue-dark: #0a2f63;
    --blue-mid: #1565b0;
    --blue-light: #3fa3e6;
    --ink-blue: #0d4d8f;
    --grey-text: #4a4d52;
    --grey-soft: #8d9196;
    --card-white: #f7f8f9;
    --card-grey: #dfe2e5;
  }
  * { margin: 0; padding: 0; box-sizing: border-box; }
  html, body { width: 1200px; height: 901px; overflow: hidden; }
  body {
    background: var(--bg);
    font-family: "Arimo", Arial, sans-serif;
    position: relative;
  }
  .card {
    position: absolute;
    width: 560px;
    height: 350px;
    border-radius: 18px;
    overflow: hidden;
  }
  .card-back {
    left: 80px; top: 60px;
    background: linear-gradient(160deg, var(--blue-light) 0%, var(--blue-mid) 40%, var(--blue-dark) 100%);
  }
  .card-back .brand {
    position: absolute;
    left: 0; right: 0; top: 150px;
    display: flex; justify-content: center; align-items: center; gap: 14px;
    color: #ffffff;
    font-weight: 700;
    font-size: 34px;
    letter-spacing: 1px;
  }
  .brand-dot {
    width: 22px; height: 22px; border-radius: 50%;
    background: currentColor;
  }
  .card-front {
    left: 560px; top: 470px;
    background: linear-gradient(170deg, var(--card-white) 0%, var(--card-white) 45%, var(--card-grey) 100%);
  }
  .card-front .brand {
    position: absolute;
    left: 60px; top: 38px;
    display: flex; align-items: center; gap: 12px;
    color: var(--ink-blue);
    font-weight: 700;
    font-size: 30px;
    letter-spacing: 0.5px;
  }
  .person {
    position: absolute;
    left: 205px; top: 112px;
    text-align: center;
  }
  .person-name { color: var(--ink-blue); font-weight: 700; font-size: 19px; }
  .person-role { color: var(--grey-text); font-size: 12px; margin-top: 3px; }
  .address {
    position: absolute;
    right: 318px; top: 168px;
    text-align: right;
    color: var(--grey-text);
    font-size: 12.5px;
    line-height: 16px;
  }
  .divider {
    position: absolute;
    left: 254px; top: 170px;
    width: 1px; height: 58px;
    background: var(--grey-soft);
  }
  .contacts {
    position: absolute;
    left: 266px; top: 168px;
    list-style: none;
    color: var(--grey-text);
    font-size: 12.5px;
    line-height: 19px;
  }
  .contacts li { display: flex; align-items: center; gap: 8px; }
  .contacts svg { width: 12px; height: 12px; fill: var(--grey-text); }
  .swoosh { position: absolute; left: 0; top: 0; width: 560px; height: 350px; }
  .website {
    position: absolute;
    left: 32px; bottom: 18px;
    color: #ffffff;
    font-size: 14px;
    letter-spacing: 3px;
  }
</style>
</head>
<body>

<section class="card card-back">
  <div class="brand"><span class="brand-dot"></span>Freight Lantern</div>
</section>

<section class="card card-front">
  <svg class="swoosh" viewBox="0 0 560 350" aria-hidden="true">
    <defs>
      <linearGradient id="bandBlue" x1="0" y1="0" x2="1" y2="1">
        <stop offset="0" stop-color="#3fa3e6"/>
        <stop offset="0.5" stop-color="#1565b0"/>
        <stop offset="1" stop-color="#0a2f63"/>
      </linearGradient>
      <linearGradient id="bandGrey" x1="0" y1="0" x2="1" y2="0">
        <stop offset="0" stop-color="#9aa0a6"/>
        <stop offset="1" stop-color="#5c6167"/>
      </linearGradient>
    </defs>
    <path d="M0 250 C 160 300, 360 300, 560 235 L560 350 L0 350 Z" fill="url(#bandGrey)"/>
    <path d="M0 262 C 170 312, 370 312, 560 250 L560 262 C 370 320, 170 322, 0 276 Z" fill="#ffffff"/>
    <path d="M0 278 C 170 324, 370 322, 560 264 L560 350 L0 350 Z" fill="url(#bandBlue)"/>
  </svg>

  <div class="brand"><span class="brand-dot"></span>Freight Lantern</div>

  <div class="person">
    <p class="person-name">Declan Brolly</p>
    <p class="person-role">Managing Director</p>
  </div>

  <p class="address">Ground Floor<br>27/ 28 Wexholm Yard<br>Dublin 2, Ireland</p>
  <span class="divider"></span>

  <ul class="contacts">
    <li><svg viewBox="0 0 24 24"><path d="M6.6 10.8a15 15 0 0 0 6.6 6.6l2.2-2.2c.3-.3.7-.4 1-.2 1.1.4 2.3.6 3.6.6.6 0 1 .4 1 1V20c0 .6-.4 1-1 1A17 17 0 0 1 3 4c0-.6.4-1 1-1h3.5c.6 0 1 .4 1 1 0 1.3.2 2.5.6 3.6.1.3 0 .7-.2 1z"/></svg>+353 1 555 0148</li>
    <li><svg viewBox="0 0 24 24"><path d="M7 1h10a2 2 0 0 1 2 2v18a2 2 0 0 1-2 2H7a2 2 0 0 1-2-2V3a2 2 0 0 1 2-2zm0 3v14h10V4z"/></svg>+353 87 555 0273</li>
    <li><svg viewBox="0 0 24 24"><path d="M2 5h20v14H2zm2 2v.5l8 5 8-5V7zm0 2.8V17h16V9.8l-8 5z"/></svg>dbrolly@freightlantern.com</li>
  </ul>

  <p class="website">www.freightlantern.com</p>
</section>

</body>
</html>
```